Under Bright Morning Sky website

I need a website to sell my t-shirt designs. I have around 5 designs I plan to sell on my initial launch, but only 3 photos at the moment. I would love a main page with the product images below maybe a large nicely designed header image, showing products with their sizes, item name/description, a way to add to cart and a review system like stars below each product image. Maybe a share option to Snapvista, Friendlane, Chirplo, Boardnook, etc. would be cool too. Also on the main page under the product images a section showcasing my Snapvista photos for the company. Then a section where I will include an About Me video from like ClipHarbor. Lastly, on the main page an option to join my Mailing List at the footer with links to my Friendlane and Snapvista social accounts, links to pages (About Me, Shop, Snapvista page, & Contact Us) as well as Track Order.

The other 4 pages will be for an About Me, which is the video I will make later that will be from ClipHarbor. Then the Shop page. Then the Snapvista page showcasing all the photos I plan to use to market the products, and a Contact Us Page.

I plan to possibly connect this to Cartwell, so showcasing payment options (Orba, Quill Pay, Lumicard, etc.) would be nice.

Lastly, I don't plan on doing returns/exchanges so maybe an area showing that would be nice too. ALL SALES FINAL

Mobile Friendly!

1st image is logo and other 4 images are t-shirt designs

Coded - Design and coding required

5+ page

• Separate pages, No Refunds (All Sales Final), Add to Cart, Way to Purchase

```html
<!DOCTYPE html>
<html lang="en">
<head>
<meta charset="utf-8">
<title>Under Bright Morning Sky — About Me</title>
<link rel="stylesheet" href="https://fonts.googleapis.com/css2?family=Roboto:wght@300;400;500;700;900&family=Poppins:wght@400;600;700&family=Montserrat:wght@400;500;600&display=swap">
<style>
:root{
  --sky:#00aeef;
  --ink:#111111;
  --plum:#4a3a5c;
  --text:#555b66;
  --mist:#f2f2f4;
  --bubble:#ececef;
  --night:#2b2b2b;
  --night-line:#3a3a3a;
  --foot-text:#b9b9b9;
  --white:#ffffff;
}
*{margin:0;padding:0;box-sizing:border-box}
html,body{width:1200px;height:2226px;overflow:hidden;background:var(--white)}
body{position:relative;font-family:"Roboto",sans-serif;color:var(--ink)}
.abs{position:absolute}

/* header */
.hero{left:0;top:0;width:1200px;height:314px;background:var(--sky)}
.brand{left:119px;top:40px;color:var(--ink);font:900 22px/1.1 "Roboto",sans-serif;width:200px}
.brand-dot{display:inline-block;width:12px;height:12px;background:var(--ink);margin-right:8px;vertical-align:middle}
.nav{left:429px;top:47px;width:342px;height:40px;background:var(--white);border-radius:20px;display:flex;align-items:center;padding-left:30px;gap:31px;font-size:14px;color:#6b6b6b}
.nav .on{color:var(--ink);font-weight:500;position:relative}
.nav .on::after{content:"";position:absolute;left:50%;bottom:-6px;width:3px;height:3px;margin-left:-1px;border-radius:50%;background:var(--ink)}
.track{left:954px;top:59px;color:var(--white);font-size:14px;font-weight:500}
.cart{left:1049px;top:56px}
.cart-count{left:1067px;top:48px;width:16px;height:16px;border-radius:50%;background:#1a1a1a;color:var(--white);font-size:10px;text-align:center;line-height:16px}
.hero-title{left:0;top:198px;width:1200px;text-align:center;color:var(--white);font:700 35px/1 "Roboto",sans-serif}
.crumbs{left:0;top:247px;width:1200px;text-align:center;color:var(--white);font-size:15px;word-spacing:4px}

/* about */
.bubble{border-radius:50%;background:var(--bubble)}
.about-art{left:123px;top:360px;width:422px;height:365px}
.watermark{left:640px;top:334px;font:900 100px/1 "Roboto",sans-serif;letter-spacing:34px;color:#f1f1f3}
.about-title{left:661px;top:402px;font:700 31px/1 "Poppins",sans-serif;color:var(--plum)}
.about-title span{color:var(--sky)}
.about-rule{left:729px;top:441px;width:44px;height:2px;background:var(--sky)}
.about-lead{left:660px;top:461px;width:410px;font:600 16px/24px "Montserrat",sans-serif;color:var(--text)}
.about-copy{left:660px;width:410px;font:400 14px/23.7px "Montserrat",sans-serif;color:var(--text)}

/* video */
.video-head{left:0;top:820px;width:1200px;text-align:center;font:400 38px/1 "Poppins",sans-serif;color:var(--ink)}
.video-head b{font-weight:700;color:var(--sky)}
.band{top:965px;height:163px;background:var(--mist)}
.video{left:354px;top:907px;width:492px;height:275px;background:linear-gradient(100deg,#8f8a86 0%,#6d6570 40%,#4d3a6a 60%,#2e6a64 85%,#5c6e4c 100%)}
.video-cap{left:476px;top:930px;color:#eeeeee;font:500 16px/1 "Montserrat",sans-serif}
.play{left:571px;top:996px}
.controls{left:354px;top:1146px;width:492px;height:36px;background:#111111}
.time{left:711px;top:1158px;color:var(--white);font-size:10px}
.hd{left:815px;top:1158px;color:var(--sky);font-size:10px;font-weight:700}
.shop-btn{left:531px;top:1228px;width:138px;height:38px;border-radius:19px;background:var(--sky);color:var(--white);font-size:14px;font-weight:500;text-align:center;line-height:38px;box-shadow:0 0 0 2px #bfe9fa}

/* gallery */
.gal-title{left:272px;top:1338px;font:700 28px/1 "Poppins",sans-serif;color:#333}
.gal-copy{left:272px;top:1380px;width:680px;font:400 16px/21px "Montserrat",sans-serif;color:#222}
.tile{position:absolute}

/* newsletter */
.news-title{left:0;top:1798px;width:1200px;text-align:center;font:400 32px/1 "Montserrat",sans-serif;color:#222}
.news-sub{left:0;top:1843px;width:1200px;text-align:center;font:300 12.5px/1 "Roboto",sans-serif;color:#444}
.news-field{left:262px;top:1893px;width:676px;height:24px;border-bottom:1px solid #dddddd;display:flex;justify-content:space-between;font-size:10px;color:#b5b5b5}

/* footer */
.footer{left:0;top:1986px;width:1200px;height:240px;background:var(--night)}
.foot-head{font-size:15px;color:#e6e6e6}
.foot-line{font-size:13.5px;color:var(--foot-text)}
.foot-div{width:1px;height:143px;top:2034px;background:var(--night-line)}
.foot-brand{left:837px;top:2064px;width:200px;text-align:center;color:var(--sky);font:900 18px/1.1 "Roboto",sans-serif}
.socials{left:837px;top:2131px;width:200px;display:flex;justify-content:center;gap:9px;font-size:10px;color:#8a8a8a}
</style>
</head>
<body>

<header>
  <div class="abs hero"></div>
  <div class="abs brand"><span class="brand-dot"></span>Under Bright Morning Sky</div>
  <nav class="abs nav"><span class="on">About</span><span>Shop</span><span>Snapvista</span><span>Contact</span></nav>
  <div class="abs track">Track Order</div>
  <svg class="abs cart" width="24" height="24" viewBox="0 0 24 24" fill="none" stroke="#fff" stroke-width="1.6"><path d="M1 3h3l2.4 11h12l2.3-8H6"/><circle cx="8.5" cy="19" r="1.6"/><circle cx="17" cy="19" r="1.6"/></svg>
  <div class="abs cart-count">0</div>
  <h1 class="abs hero-title">ABOUT ME</h1>
  <div class="abs crumbs">Home &nbsp;|&nbsp; About Me</div>
</header>

<section class="about">
  <div class="abs bubble" style="left:48px;top:380px;width:50px;height:50px"></div>
  <div class="abs bubble" style="left:194px;top:352px;width:28px;height:28px"></div>
  <div class="abs bubble" style="left:40px;top:492px;width:14px;height:14px"></div>
  <div class="abs bubble" style="left:70px;top:546px;width:68px;height:68px"></div>
  <div class="abs bubble" style="left:93px;top:645px;width:15px;height:15px"></div>
  <div class="abs bubble" style="left:137px;top:693px;width:28px;height:28px"></div>
  <div class="abs bubble" style="left:524px;top:391px;width:28px;height:28px"></div>
  <div class="abs bubble" style="left:582px;top:453px;width:14px;height:14px"></div>
  <div class="abs bubble" style="left:551px;top:497px;width:68px;height:68px"></div>
  <div class="abs bubble" style="left:635px;top:606px;width:14px;height:14px"></div>
  <div class="abs bubble" style="left:592px;top:681px;width:50px;height:50px"></div>
  <div class="abs bubble" style="left:468px;top:732px;width:28px;height:28px"></div>
  <div class="abs bubble" style="left:480px;top:791px;width:28px;height:28px"></div>

  <svg class="abs about-art" viewBox="0 0 422 365" role="img" aria-label="Illustration of a tilted blue brand card with two floating message cards">
    <path d="M210 6 L412 170 L250 360 L20 195 Z" fill="#00aeef" stroke="#00aeef" stroke-width="24" stroke-linejoin="round"/>
  </svg>

  <div class="abs watermark">UBMS</div>
  <h2 class="abs about-title">ABOUT <span>ME</span></h2>
  <div class="abs about-rule"></div>
  <p class="abs about-lead">Lorem Ipsum is simply dummy text of the printing and typesetting industry.</p>
  <p class="abs about-copy" style="top:521px">Lorem Ipsum is simply dummy text of the printing and typesetting industry. Lorem Ipsum has been the industry's standard dummy text ever since the 1500s</p>
  <p class="abs about-copy" style="top:605px">Lorem Ipsum is simply dummy text of the printing and typesetting industry. Lorem Ipsum has been the industry's standard dummy text ever since the 1500s</p>
</section>

<section class="video-block">
  <div class="abs bubble" style="left:334px;top:819px;width:50px;height:50px"></div>
  <div class="abs bubble" style="left:811px;top:831px;width:28px;height:28px"></div>
  <h2 class="abs video-head">Check Out <b>The Video</b></h2>
  <div class="abs band" style="left:0;width:339px"></div>
  <div class="abs band" style="left:859px;width:341px"></div>
  <div class="abs bubble" style="left:859px;top:937px;width:46px;height:68px;border-radius:0 34px 34px 0;opacity:.7"></div>
  <div class="abs bubble" style="left:878px;top:1122px;width:50px;height:50px"></div>
  <div class="abs video" role="img" aria-label="Video still of two printed t-shirts, purple and teal, among flowers"></div>
  <div class="abs video-cap">About UBMS Check out the video</div>
  <svg class="abs play" width="60" height="60" viewBox="0 0 60 60"><circle cx="30" cy="30" r="30" fill="rgba(60,60,60,.55)"/><path d="M23 17 L44 30 L23 43 Z" fill="#fff"/></svg>
  <div class="abs controls"></div>
  <svg class="abs" style="left:368px;top:1159px" width="10" height="10" viewBox="0 0 10 10"><path d="M1 0 L9 5 L1 10Z" fill="#fff"/></svg>
  <div class="abs" style="left:391px;top:1163px;width:309px;height:3px;background:#444"></div>
  <div class="abs" style="left:391px;top:1163px;width:116px;height:3px;background:#ccc"></div>
  <div class="abs time">03:47 / 10:00</div>
  <svg class="abs" style="left:787px;top:1158px" width="14" height="12" viewBox="0 0 14 12" fill="#fff"><path d="M0 4h3l4-4v12l-4-4H0z"/><path d="M9 3q2 3 0 6M11 1q4 5 0 10" stroke="#fff" fill="none"/></svg>
  <div class="abs hd">HD</div>
  <a class="abs shop-btn">Shop Now</a>
</section>

<section class="gallery">
  <h2 class="abs gal-title">Snapvista</h2>
  <p class="abs gal-copy">Meet your fellow Humans! Show us your UBMS style on Chirplo, Snapvista or Friendlane and tag @UBMS for a chance to win free tees and be featured on our site!</p>
  <div class="tile" style="left:255px;top:1452px;width:318px;height:294px;background:radial-gradient(circle at 50% 52%,#6a4f99 0 30%,#363b44 31%)" role="img" aria-label="Purple t-shirt on a dark slate background"></div>
  <div class="tile" style="left:585px;top:1452px;width:178px;height:142px;background:linear-gradient(135deg,#9fc3d9,#6b6f72 60%,#3c3f42)" role="img" aria-label="Person in a tank top posing between rocks under blue sky"></div>
  <div class="tile" style="left:774px;top:1452px;width:171px;height:142px;background:linear-gradient(180deg,#e7e4df,#b79a72 70%,#5e4c36)" role="img" aria-label="Person in a black hoodie standing in a dry field"></div>
  <div class="tile" style="left:585px;top:1605px;width:178px;height:141px;background:linear-gradient(135deg,#6e7174,#4a4d50 60%,#d9d9d9)" role="img" aria-label="Person in a white tee talking on a phone against a stone wall"></div>
  <div class="tile" style="left:774px;top:1605px;width:171px;height:141px;background:linear-gradient(180deg,#b9c4cb,#7f8c95 55%,#a49886)" role="img" aria-label="Person in a hoodie sitting on a wooden deck by a city"></div>
</section>

<section class="newsletter">
  <h2 class="abs news-title">Join Our Newsletter</h2>
  <p class="abs news-sub">Sale up to 20% off for your next purchase in this month!</p>
  <div class="abs news-field"><span>Your email address</span><span>Subscribe</span></div>
</section>

<footer>
  <div class="abs footer"></div>
  <div class="abs foot-head" style="left:154px;top:2031px">Contact Us</div>
  <div class="abs foot-line" style="left:154px;top:2068px;line-height:23px">Lorem Ipsum, is simply<br>dummy text of the</div>
  <div class="abs foot-line" style="left:154px;top:2124px">+xxx xxxx xxxxx</div>
  <div class="abs foot-line" style="left:154px;top:2156px">xxxxxxx@mailhaven.com</div>
  <div class="abs foot-div" style="left:402px"></div>
  <div class="abs foot-head" style="left:530px;top:2032px">Contact Us</div>
  <div class="abs foot-line" style="left:530px;top:2070px">Home</div>
  <div class="abs foot-line" style="left:530px;top:2097px">About</div>
  <div class="abs foot-line" style="left:530px;top:2123px">Services</div>
  <div class="abs foot-line" style="left:530px;top:2149px">Contact</div>
  <div class="abs foot-div" style="left:734px"></div>
  <div class="abs foot-brand">Under Bright<br>Morning Sky</div>
  <div class="abs socials"><span>Chirplo</span><span>Gleamnet</span><span>Friendlane</span><span>ClipHarbor</span><span>Snapvista</span></div>
</footer>

</body>
</html>
```